I am looking for a book cover designs. The title of the book is "Ways to stand out and where your habits slip"

the book is not too formal but it is also not informal.

I wish for the title to be easily readable and capturing, especially the "ways to stand out" part.

the book should also include the author name: Tobar Kessly

everyone

• Full title and author name: Tobar Kessly
• There is a chapter that is called "turn the lamp inward", if you wish to do an illustration as part of the cover then perhaps that can give you an idea of what to go with.
• anything that takes attention away from the title.Also should not include any photographs.

```html
<!DOCTYPE html>
<html lang="en">
<head>
<meta charset="UTF-8">
<title>Ways to Stand Out — Tobar Kessly</title>
<link href="https://fonts.googleapis.com/css2?family=Great+Vibes&family=Montserrat:wght@700&family=Oswald:wght@500&display=swap" rel="stylesheet">
<style>
  :root {
    --paper: #f4ddd3;
    --blush: #ecc9bb;
    --rose: #e2b4a3;
    --ink: #553f1c;
    --frame: #b49c9c;
    --frame-thin: #a58e8e;
    --lens: #a79b97;
  }
  html, body {
    margin: 0;
    padding: 0;
    width: 752px;
    height: 1200px;
    overflow: hidden;
    background: var(--paper);
  }
  .cover {
    position: relative;
    width: 752px;
    height: 1200px;
    overflow: hidden;
  }
  .cover__backdrop {
    position: absolute;
    inset: 0;
    background:
      radial-gradient(ellipse 260px 420px at 640px 360px, var(--blush) 0%, rgba(236,201,187,0) 100%),
      radial-gradient(ellipse 420px 300px at 330px 1000px, var(--rose) 0%, rgba(226,180,163,0) 100%),
      radial-gradient(ellipse 140px 420px at 380px 260px, var(--blush) 0%, rgba(236,201,187,0) 100%),
      linear-gradient(180deg, #f1d8cd 0%, var(--paper) 55%, #efcfc2 100%);
  }
  .cover__frame {
    position: absolute;
    inset: 0;
  }
  .cover__lens {
    position: absolute;
    left: 0;
    top: 0;
    opacity: 0.75;
  }
  .title {
    position: absolute;
    inset: 0;
    margin: 0;
    font-family: "Great Vibes", cursive;
    font-weight: 400;
    color: var(--ink);
    line-height: 1;
  }
  .title__line {
    position: absolute;
    white-space: nowrap;
    transform: translate(-50%, -50%) rotate(-22deg);
  }
  .title__line--one   { left: 260px; top: 330px; font-size: 170px; }
  .title__line--two   { left: 370px; top: 470px; font-size: 150px; }
  .title__line--three { left: 420px; top: 600px; font-size: 170px; }
  .subtitle {
    position: absolute;
    left: 0;
    right: 0;
    top: 780px;
    margin: 0;
    text-align: center;
    padding-left: 70px;
    font-family: "Montserrat", sans-serif;
    font-weight: 700;
    font-size: 29px;
    letter-spacing: 0.16em;
    line-height: 42px;
    color: var(--ink);
    text-transform: uppercase;
  }
  .author {
    position: absolute;
    left: 0;
    right: 0;
    top: 1019px;
    margin: 0;
    text-align: center;
    font-family: "Oswald", sans-serif;
    font-weight: 500;
    font-size: 34px;
    letter-spacing: 0.14em;
    line-height: 44px;
    color: var(--ink);
    text-transform: uppercase;
  }
  .author-rules {
    position: absolute;
    left: 0;
    top: 0;
  }
</style>
</head>
<body>
<main class="cover">
  <div class="cover__backdrop" role="img" aria-label="Soft blush painted brush-stroke shapes forming the background"></div>

  <svg class="cover__lens" width="752" height="1200" viewBox="0 0 752 1200" aria-hidden="true">
    <circle cx="501" cy="779" r="60" fill="none" stroke="var(--lens)" stroke-width="24"/>
    <line x1="552" y1="832" x2="682" y2="880" stroke="var(--lens)" stroke-width="28" stroke-linecap="round"/>
  </svg>

  <svg class="cover__frame" width="752" height="1200" viewBox="0 0 752 1200" aria-hidden="true">
    <path d="M46 13 H706 A33 33 0 0 0 739 46 V1154 A33 33 0 0 0 706 1187 H46 A33 33 0 0 0 13 1154 V46 A33 33 0 0 0 46 13 Z"
          fill="none" stroke="var(--frame)" stroke-width="6"/>
    <path d="M52 33 H700 A18 18 0 0 0 718 51 V1149 A18 18 0 0 0 700 1167 H52 A18 18 0 0 0 34 1149 V51 A18 18 0 0 0 52 33 Z"
          fill="none" stroke="var(--frame-thin)" stroke-width="1.2"/>
  </svg>

  <h1 class="title">
    <span class="title__line title__line--one">Ways</span>
    <span class="title__line title__line--two">To Stand</span>
    <span class="title__line title__line--three">Out</span>
  </h1>

  <p class="subtitle">And where your<br>habits slip</p>

  <svg class="author-rules" width="752" height="1200" viewBox="0 0 752 1200" aria-hidden="true">
    <g fill="none" stroke="#8d7272" stroke-width="1.5">
      <line x1="234" y1="1020" x2="523" y2="1020"/>
      <line x1="234" y1="1063" x2="523" y2="1063"/>
      <rect x="226" y="1016" width="7" height="7" transform="rotate(45 229.5 1019.5)"/>
      <rect x="524" y="1016" width="7" height="7" transform="rotate(45 527.5 1019.5)"/>
      <rect x="226" y="1059" width="7" height="7" transform="rotate(45 229.5 1062.5)"/>
      <rect x="524" y="1059" width="7" height="7" transform="rotate(45 527.5 1062.5)"/>
    </g>
  </svg>
  <p class="author">Tobar Kessly</p>
</main>
</body>
</html>
```